Brighter Than Dawn Home Entertainment

We are a home theater installation company focus on front projection system and home theater surround system. We built highend home theater for people to enjoy movie, sports and gaming on big screen at home.
I'm looking for a dispaly to showcase our work as well as help people build their home theater

Number of Pages Required

3 page

Colors

Designer to choose colors to be used in the design.

Requirements
Must have
• Home Page
• What we do
• Who we are
• Gallery
• Contact Us
Nice to have
• Picture jump out of big screen make a 3D feeling

```html
<!DOCTYPE html>
<html lang="en">
<head>
<meta charset="utf-8">
<title>Brighter Than Dawn Home Entertainment</title>
<link href="https://fonts.googleapis.com/css2?family=Bebas+Neue&family=Montserrat:wght@400;500&family=Arimo:wght@400&display=swap" rel="stylesheet">
<style>
:root{
  --bg:#1f1f1f;
  --bg-header:#2a2a2a;
  --bg-dark:#161616;
  --text:#ffffff;
  --muted:#d6d6d6;
  --line:rgba(255,255,255,.75);
  --field:rgba(12,12,12,.55);
}
*{box-sizing:border-box;margin:0;padding:0}
html,body{width:1200px;height:2804px;overflow:hidden;background:var(--bg);color:var(--text);font-family:"Arimo",Arial,sans-serif}
.page{position:relative;width:1200px;height:2804px}
.abs{position:absolute}
.heading{font-family:"Bebas Neue",Impact,sans-serif;font-weight:400;letter-spacing:1px;line-height:1;white-space:nowrap}
.body-copy{font-size:14.5px;line-height:26px;color:var(--muted)}
.btn{position:absolute;border:1.5px solid var(--line);color:var(--text);font-family:"Montserrat",Arial,sans-serif;font-size:18px;display:flex;align-items:center;justify-content:center;letter-spacing:.5px}

/* header */
.site-header{left:0;top:0;width:1200px;height:104px;background:var(--bg-header)}
.brand{left:77px;top:41px;font-family:"Montserrat",Arial,sans-serif;font-size:18px;font-weight:500;color:var(--text);white-space:nowrap}
.nav{right:77px;top:44px;display:flex;gap:42px;font-family:"Montserrat",Arial,sans-serif;font-size:14px}
.nav .active{position:relative}
.nav .active::after{content:"";position:absolute;left:-6px;right:-6px;top:51px;height:2px;background:#888}

/* hero */
.hero{left:0;top:104px;width:1200px;height:552px;background:linear-gradient(100deg,#1a1512 0%,#2e2520 35%,#3a3030 60%,#1d2a3a 80%,#2a2024 100%)}
.hero-title{left:77px;top:268px;font-size:62px}
.hero-text{left:79px;top:336px;width:380px;font-size:15px;line-height:28px;color:var(--text)}

/* who */
.who-image{left:84px;top:738px;width:421px;height:393px;background:linear-gradient(160deg,#4a4a4a,#2a2a2a 55%,#d9d9d9 85%,#bdbdbd)}
.who-title{left:590px;top:748px;font-size:62px}
.who-text{left:590px;top:822px;width:515px}

/* what */
.what{left:0;top:1210px;width:1200px;height:428px;background:linear-gradient(90deg,#2a2c2c,#3a3a38 40%,#2e2e2e 60%,#353535)}
.what-title{left:0;top:1260px;width:1200px;text-align:center;font-size:61px}
.what-intro{left:250px;top:1336px;width:700px;text-align:center;font-size:14.5px;line-height:26px;color:var(--muted)}
.service-title{font-family:"Montserrat",Arial,sans-serif;font-size:21px;white-space:nowrap}
.service-text{font-size:14px;line-height:25px;color:var(--muted)}
.icon-ring{width:112px;height:112px}

/* gallery */
.gallery-title{left:0;top:1690px;width:1200px;text-align:center;font-size:64px}
.tile{width:333px;height:208px}

/* contact */
.contact{left:0;top:2312px;width:1200px;height:418px;background:linear-gradient(90deg,#1c1c1c,#2a2a2a 50%,#222)}
.contact-card{left:77px;top:2387px;width:309px;height:293px;border:1px solid rgba(255,255,255,.35)}
.card-title{left:100px;top:2422px;font-size:26.5px}
.card-rule{left:100px;top:2468px;width:260px;height:1px;background:rgba(255,255,255,.3)}
.contact-row{left:102px;display:flex;gap:14px;font-size:14px;line-height:24px;color:var(--muted)}
.quote-title{left:442px;top:2381px;font-size:38px}
.quote-rule{left:442px;top:2440px;width:680px;height:1px;background:rgba(255,255,255,.3)}
.field{background:var(--field);font-size:14px;color:#aaa;padding:13px 16px}
.send{left:1060px;top:2487px;width:62px;height:145px;background:#fff;display:flex;align-items:center;justify-content:center}
.footer{left:0;top:2730px;width:1200px;height:74px;background:var(--bg-dark);display:flex;align-items:center;justify-content:center;font-family:"Montserrat",Arial,sans-serif;font-size:14px;color:var(--muted)}
</style>
</head>
<body>
<div class="page">

<header class="abs site-header">
  <div class="abs brand">Brighter Than Dawn Home Entertainment</div>
  <nav class="abs nav"><span class="active">HOME</span><span>ABOUT</span><span>SERVICES</span><span>GALLARY</span><span>CONTACT</span></nav>
</header>

<section class="abs hero" role="img" aria-label="Couple relaxing on a rug watching a projected film, a creature emerging from the screen over a night city view"></section>
<h1 class="abs heading hero-title">BRIGHTER THAN DAWN</h1>
<p class="abs hero-text">Lorem Ipsum is simply dummy text of the printing and typesetting industry. Lorem Ipsum has been.</p>
<div class="btn" style="left:77px;top:424px;width:188px;height:52px">KNOW MORE</div>

<div class="abs who-image" role="img" aria-label="Framed movie still beside a projector, ceiling mount and HDMI cable"></div>
<h2 class="abs heading who-title">WHO WE ARE</h2>
<div class="abs who-text body-copy">
  <p>Lorem Ipsum is simply dummy text of the printing and typesetting industry. Lorem Ipsum has been the industry's standard dummy text ever since the 1500s, when an unknown printer took a galley of type and scrambled it to make a type specimen book. It has survived not only five centuries, but also the leap into electronic typesetting.</p>
  <p style="margin-top:16px">Lorem Ipsum is simply dummy text of the printing and typesetting industry Lorem Ipsum has been the industry's standard dummy text ever since the.</p>
</div>
<div class="btn" style="left:588px;top:1045px;width:187px;height:50px">KNOW MORE</div>

<section class="abs what" role="img" aria-label="Dim backdrop of a coastal landscape and a living room"></section>
<h2 class="abs heading what-title">WHAT WE DO</h2>
<p class="abs what-intro">Lorem Ipsum is simply dummy text of the printing and typesetting industry. Lorem Ipsum has been the industry's standard dummy text ever since.</p>

<div class="abs service-title" style="right:788px;top:1434px;text-align:right">Front projection system</div>
<p class="abs service-text" style="left:90px;top:1472px;width:322px;text-align:right">Lorem ipsum dolor sit amet, consectetur adipiscing elit. Nam tempor faucibus ante, eget vulputate libero pharetra eu. Nulla at felis eros.</p>
<svg class="abs icon-ring" style="left:450px;top:1432px" viewBox="0 0 112 112" aria-hidden="true">
  <circle cx="56" cy="56" r="52" fill="none" stroke="#fff" stroke-width="4"/>
  <circle cx="56" cy="56" r="45" fill="none" stroke="#fff" stroke-width="1.5"/>
  <rect x="34" y="47" width="44" height="20" rx="3" fill="none" stroke="#fff" stroke-width="2.5"/>
  <circle cx="66" cy="57" r="6" fill="none" stroke="#fff" stroke-width="2.5"/>
  <line x1="40" y1="54" x2="54" y2="54" stroke="#fff" stroke-width="2"/>
  <line x1="40" y1="60" x2="54" y2="60" stroke="#fff" stroke-width="2"/>
  <line x1="40" y1="67" x2="40" y2="71" stroke="#fff" stroke-width="2.5"/>
  <line x1="72" y1="67" x2="72" y2="71" stroke="#fff" stroke-width="2.5"/>
</svg>
<svg class="abs icon-ring" style="left:636px;top:1432px" viewBox="0 0 112 112" aria-hidden="true">
  <circle cx="56" cy="56" r="52" fill="none" stroke="#fff" stroke-width="4"/>
  <circle cx="56" cy="56" r="45" fill="none" stroke="#fff" stroke-width="1.5"/>
  <rect x="32" y="40" width="12" height="32" fill="none" stroke="#fff" stroke-width="2.5"/>
  <rect x="68" y="40" width="12" height="32" fill="none" stroke="#fff" stroke-width="2.5"/>
  <rect x="47" y="44" width="18" height="26" fill="none" stroke="#fff" stroke-width="2.5"/>
  <circle cx="38" cy="50" r="3" fill="#fff"/><circle cx="38" cy="63" r="4" fill="none" stroke="#fff" stroke-width="2"/>
  <circle cx="74" cy="50" r="3" fill="#fff"/><circle cx="74" cy="63" r="4" fill="none" stroke="#fff" stroke-width="2"/>
  <circle cx="56" cy="52" r="3" fill="none" stroke="#fff" stroke-width="2"/><circle cx="56" cy="62" r="3" fill="none" stroke="#fff" stroke-width="2"/>
</svg>
<div class="abs service-title" style="left:788px;top:1434px">Home theater surround</div>
<p class="abs service-text" style="left:788px;top:1472px;width:330px">Lorem ipsum dolor sit amet, consectetur adipiscing elit. Nam tempor faucibus ante, eget vulputate libero pharetra eu. Nulla at felis eros.</p>

<h2 class="abs heading gallery-title">PROJECT GALLARY</h2>
<div class="abs tile" style="left:77px;top:1780px;background:linear-gradient(180deg,#1b2bd0,#2a1a8a 60%,#4a4a70)" role="img" aria-label="Blue-lit home cinema with tiered seating"></div>
<div class="abs tile" style="left:433px;top:1780px;background:linear-gradient(180deg,#7a6a58,#5a6a5a 45%,#8a7a62)" role="img" aria-label="Living room with a landscape on a wall screen"></div>
<div class="abs tile" style="left:789px;top:1780px;background:linear-gradient(180deg,#3a3432,#5a4a42 45%,#2a2a2a)" role="img" aria-label="Dark theater room with leather sofas and white screen"></div>
<div class="abs tile" style="left:77px;top:2012px;background:linear-gradient(160deg,#d8d8d8,#3a3a3a 50%,#8a8078)" role="img" aria-label="Black and white theater room with curved screen"></div>
<div class="abs tile" style="left:433px;top:2012px;background:linear-gradient(180deg,#6a3a34,#d8d2cc 60%,#6a6a6a)" role="img" aria-label="Media wall with television and shelving"></div>
<div class="abs tile" style="left:789px;top:2012px;background:linear-gradient(180deg,#5a5448,#4a5a48 45%,#7a2020)" role="img" aria-label="Lounge with projected mountain scene and red seating"></div>

<section class="abs contact" role="img" aria-label="Dim backdrop of a theater room with mountain view"></section>
<div class="abs contact-card"></div>
<h3 class="abs heading card-title">CONTACT DETAIL</h3>
<div class="abs card-rule"></div>
<div class="abs contact-row" style="top:2488px">
  <svg width="18" height="24" viewBox="0 0 18 24" aria-hidden="true"><path d="M9 1C4.6 1 1.5 4.3 1.5 8.5 1.5 14 9 23 9 23s7.5-9 7.5-14.5C16.5 4.3 13.4 1 9 1z" fill="#fff"/><circle cx="9" cy="8.5" r="3" fill="#222"/></svg>
  <span>Lorem Ipsum is simply dummy<br>text of the printing.</span>
</div>
<div class="abs contact-row" style="top:2560px">
  <svg width="18" height="18" viewBox="0 0 24 24" aria-hidden="true"><path d="M6.6 10.8a15 15 0 0 0 6.6 6.6l2.2-2.2c.3-.3.7-.4 1-.2 1.1.4 2.3.6 3.6.6.6 0 1 .4 1 1V20c0 .6-.4 1-1 1A17 17 0 0 1 3 4c0-.6.4-1 1-1h3.5c.6 0 1 .4 1 1 0 1.3.2 2.5.6 3.6.1.3 0 .7-.2 1z" fill="#fff"/></svg>
  <span>123 456 7890</span>
</div>
<div class="abs contact-row" style="top:2597px">
  <svg width="18" height="18" viewBox="0 0 24 24" aria-hidden="true"><rect x="2" y="5" width="20" height="14" rx="1" fill="none" stroke="#fff" stroke-width="2"/><path d="M3 6l9 7 9-7" fill="none" stroke="#fff" stroke-width="2"/></svg>
  <span>info@brighterthandawn.com</span>
</div>

<h3 class="abs heading quote-title">REQUEST A FREE QUOTE</h3>
<div class="abs quote-rule"></div>
<div class="abs field" style="left:450px;top:2487px;width:280px;height:43px">Name</div>
<div class="abs field" style="left:450px;top:2539px;width:280px;height:43px">Email</div>
<div class="abs field" style="left:450px;top:2591px;width:280px;height:43px">Phone</div>
<div class="abs field" style="left:745px;top:2487px;width:302px;height:145px">Message</div>
<div class="abs send"><svg width="26" height="22" viewBox="0 0 26 22" aria-hidden="true"><path d="M1 11 25 1 19 21 12 14z" fill="#222"/><path d="M12 14 25 1" stroke="#fff" stroke-width="1.5"/></svg></div>

<footer class="abs footer">2018 ©BRIGHTER THAN DAWN- All Rights Reserved.</footer>
</div>
</body>
</html>
```